Business Card Design.

Life and Wellness Coach
www.brightpathwell.com
Want to use my name as the logo it could be the initials TRH or my full name. I want to trade mark me.
I like clean lines and simple designs, but it pops using the colors scheme (one or two colors) on the website.
I provide life and health coaching virtually and in person. My services include: Nutrition Response Testing, Allergy Elimination Testing, Wellness Coaching, Life Coaching. Life and Health Assessments, and I sell foundational health products and specialized nutrition. Use colors that represent healing and trust.
Target Market(s)
Women for the ages of 30 - 60
Industry/Entity Type
Health
Contact Information for Business Card
Tessa Ravenna Holloway
Life and Wellness Coach
tessa@coachtrh.com
www.brightpathwell.com
443-781-6392
Health is not an event it's a lifestyle (tag line or if you have a better tag line)

```html
<!DOCTYPE html>
<html lang="en">
<head>
<meta charset="utf-8">
<title>Tessa Ravenna Holloway – Business Card</title>
<link rel="stylesheet" href="https://fonts.googleapis.com/css2?family=Cormorant+Garamond:ital,wght@1,500;1,600&family=Arimo:wght@400&display=swap">
<style>
  :root {
    --page-bg: #e9e6e3;
    --card-white: #ffffff;
    --rose: #b8457a;
    --rose-light: #cf6f98;
    --rose-deep: #a52d63;
    --sky: #4bb3e2;
    --sky-deep: #1f8fcb;
    --name-muted: #7d6a96;
    --portrait-dark: #6b4a3c;
    --portrait-warm: #c9a08a;
    --portrait-blue: #3c4f9a;
    --text-light: #ffffff;
  }
  * { box-sizing: border-box; margin: 0; padding: 0; }
  html, body { width: 1200px; height: 914px; overflow: hidden; }
  body {
    background: var(--page-bg);
    display: flex;
    flex-direction: column;
    align-items: center;
    justify-content: center;
    gap: 40px;
    font-family: "Arimo", Arial, sans-serif;
  }
  .card {
    position: relative;
    width: 680px;
    height: 389px;
    background: var(--card-white);
    overflow: hidden;
    box-shadow: 0 6px 18px rgba(0,0,0,.15);
  }
  .script { font-family: "Cormorant Garamond", Georgia, serif; font-style: italic; }

  /* Back side */
  .back-portrait {
    position: absolute; right: 0; bottom: 0; width: 270px; height: 310px;
    background: radial-gradient(ellipse at 55% 40%, #e9dcd4 0 30%, #cfc6c4 45%, #d9d8e6 75%, #f4f4f6 100%);
    opacity: .75;
  }
  .back-name {
    position: absolute; left: 150px; top: 40px;
    font-size: 26px; font-weight: 500; color: var(--name-muted); letter-spacing: .5px;
  }
  .tagline {
    position: absolute; left: 95px; top: 220px; text-align: right; width: 330px;
    font-size: 32px; font-weight: 600; line-height: 1.05;
  }
  .tagline .line-one { color: var(--rose); display: block; }
  .tagline .line-two { color: var(--sky-deep); display: block; }

  /* Front side */
  .front-portrait {
    position: absolute; left: 0; top: 0; width: 320px; height: 389px;
    background: radial-gradient(ellipse at 50% 38%, var(--portrait-warm) 0 28%, var(--portrait-dark) 46%, #f3f3f3 70%),
                linear-gradient(to bottom, transparent 70%, var(--portrait-blue) 70%);
  }
  .title-band {
    position: absolute; left: 340px; top: 0; width: 340px; height: 190px;
    background: linear-gradient(to bottom, var(--rose-light), var(--rose-deep));
    color: var(--text-light);
    padding: 52px 22px 0 20px;
    text-align: right;
  }
  .front-name { font-size: 28px; font-weight: 600; display: block; white-space: nowrap; }
  .role { font-size: 16px; display: block; margin-top: 4px; }
  .contact-shape { position: absolute; left: 0; top: 0; }
  .contact-list {
    position: absolute; right: 22px; top: 240px; list-style: none;
    color: var(--text-light); font-size: 19px; text-align: right; line-height: 1.4;
  }
  .contact-list li { display: flex; align-items: center; justify-content: flex-end; gap: 12px; }
  .contact-list svg { width: 18px; height: 18px; flex: none; }
</style>
</head>
<body>

<section class="card card-back">
  <div class="back-portrait" role="img" aria-label="Soft faded portrait photo of the coach"></div>
  <p class="back-name script">Tessa Ravenna Holloway</p>
  <p class="tagline script">
    <span class="line-one">Health is not an event</span>
    <span class="line-two">it's a lifestyle</span>
  </p>
</section>

<section class="card card-front">
  <div class="front-portrait" role="img" aria-label="Portrait photo of the coach smiling"></div>
  <svg class="contact-shape" width="680" height="389" viewBox="0 0 680 389" aria-hidden="true">
    <defs>
      <linearGradient id="skyFill" x1="0" y1="0" x2="0" y2="1">
        <stop offset="0" stop-color="#4bb3e2"/>
        <stop offset="1" stop-color="#1f8fcb"/>
      </linearGradient>
    </defs>
    <polygon points="340,190 680,190 680,389 230,389" fill="url(#skyFill)"/>
  </svg>
  <div class="title-band">
    <span class="front-name script">Tessa Ravenna Holloway</span>
    <span class="role">Life and Wellness Coach</span>
  </div>
  <ul class="contact-list">
    <li>443-781-6392
      <svg viewBox="0 0 24 24"><path fill="#fff" d="M6.6 10.8a15 15 0 0 0 6.6 6.6l2.2-2.2c.3-.3.7-.4 1-.2 1.1.4 2.3.6 3.6.6.6 0 1 .4 1 1V20c0 .6-.4 1-1 1A17 17 0 0 1 3 4c0-.6.4-1 1-1h3.5c.6 0 1 .4 1 1 0 1.3.2 2.5.6 3.6.1.3 0 .7-.2 1z"/></svg>
    </li>
    <li>www.brightpathwell.com
      <svg viewBox="0 0 24 24" fill="none" stroke="#fff" stroke-width="2"><circle cx="12" cy="12" r="9"/><path d="M3 12h18M12 3c3 3 3 15 0 18M12 3c-3 3-3 15 0 18"/></svg>
    </li>
    <li>tessa@coachtrh.com
      <svg viewBox="0 0 24 24" fill="none" stroke="#fff" stroke-width="2"><rect x="3" y="6" width="18" height="12"/><path d="M3 6l9 7 9-7"/></svg>
    </li>
  </ul>
</section>

</body>
</html>
```